Bluegate Gatherings Web Design Layout (no HTML)

We require the layout only for a website.  No html or logo is required - just the layout.

A refreshed and revitalized website to coincide with the relaunch of our brand. We are looking for a clean simplistic design that is easy to use and presents relevant information effectively.
We are an events management company specializing in conferences.
Updates

Thank you for your design. We really like the imagery. Essentially we are after a home page design (one page) that incorporates the 3 main buttons (request a proposal, select a venue and specials) while providing the relevant information on our service via functionality similar to that on www.trelvasite.com ie using the large arrow to scroll over the relevant topic to receive information. We hope to finalise the contest in the next week and hope to consider your revised entry.

Thanks!

Target Market(s)

Australian corporate sector primarily Managing Directors or their assistants. Any business looking to hold a conference for up 500 delegates however we are primarily targeting the decision maker so need to ensure we are communicating on their terms.

Industry/Entity Type

Event

Requirements
Must have
• Incorporate the elements from the attached document however with complete creative license as to their layout. Our main competitors are pordamhosting.com.au, brimwellsummits.com.au both sites are bland and not user friendly.
Nice to have
• Colours red, silver and black. Note we are running a separate contest to refresh our logo.
• We like the functionality of trelvasite.com

```html
<!DOCTYPE html>
<html lang="en">
<head>
<meta charset="utf-8">
<title>Bluegate Gatherings – Home</title>
<link rel="stylesheet" href="https://fonts.googleapis.com/css2?family=Questrial&family=Arimo:wght@400;700&display=swap">
<style>
:root{
  --black:#000;
  --white:#fff;
  --red:#e00000;
  --red-dark:#b80000;
  --red-light:#ff2020;
  --panel-grey:#e8e8e8;
  --text-grey:#777;
  --heading-grey:#666;
  --ink:#111;
  --divider:#dcdcdc;
  --tab-dark:#3a3a3a;
}
*{box-sizing:border-box;margin:0;padding:0}
html,body{width:1200px;height:735px;overflow:hidden}
body{position:relative;background:var(--black);font-family:"Questrial",sans-serif;color:var(--ink)}
.band{position:absolute;left:0;top:102px;width:1200px;height:43px;background:linear-gradient(#fafafa,#ececec)}
.frame{position:absolute;left:117px;top:8px;width:941px;height:663px;background:var(--white);border-radius:8px}
.header{position:absolute;left:125px;top:15px;width:925px;height:88px;border-radius:6px 6px 0 0;
  background:linear-gradient(90deg,#1a1a1a 0%,#6a6a6a 22%,#d8d8d8 44%,#ffffff 53%,#cfcfcf 62%,#5a5a5a 82%,#1a1a1a 100%)}
.logo-slot{position:absolute;left:167px;top:61px;font-family:"Arimo",sans-serif;font-size:11px;color:var(--white);letter-spacing:-.2px}
.search-label{position:absolute;left:738px;top:60px;font-family:"Arimo",sans-serif;font-weight:700;font-size:14px;color:var(--black)}
.search-field{position:absolute;left:807px;top:57px;width:190px;height:22px;background:var(--white);border:1px solid #999}
.search-go{position:absolute;left:999px;top:55px;width:29px;height:28px;border-radius:3px;border:1px solid #700;
  background:linear-gradient(#ff4a4a,#c40000);color:var(--white);font-family:"Arimo",sans-serif;font-weight:700;font-size:12px;line-height:26px;text-align:center}
.nav{position:absolute;left:125px;top:103px;width:925px;height:42px;background:var(--black)}
.nav ul{list-style:none}
.nav li{position:absolute;top:19px;font-size:14px;color:var(--white);letter-spacing:.1px}
.nav li.current{font-weight:700;color:#e8f0ff}
.nav-notch{position:absolute;left:215px;top:35px;width:0;height:0;border-left:7px solid transparent;border-right:7px solid transparent;border-bottom:7px solid var(--white)}
.side-menu{position:absolute;left:127px;top:206px;list-style:none}
.side-menu li{position:relative;height:30px;padding-left:19px;font-size:15px;line-height:30px;color:var(--ink)}
.side-menu li.current{color:var(--white)}
.side-menu svg{position:absolute;left:-2px;top:-1px;z-index:0}
.side-menu li span{position:relative;z-index:1}
.column-rule{position:absolute;left:270px;top:165px;width:2px;height:455px;background:linear-gradient(var(--white),var(--divider) 15%,var(--divider) 85%,var(--white))}
.intro{position:absolute;left:299px;top:170px;width:515px;font-size:18px;line-height:20.5px;color:var(--ink)}
.intro strong{font-weight:700;font-family:"Arimo",sans-serif;font-size:17px}
.finance{position:absolute;left:283px;top:253px;width:528px;height:254px;background:var(--panel-grey);border-radius:8px}
.finance h2{position:absolute;left:35px;top:11px;font-family:"Arimo",sans-serif;font-weight:700;font-size:15.5px;color:var(--heading-grey)}
.finance-art{position:absolute;left:40px;top:62px;width:100px;height:155px;border-radius:40px;background:radial-gradient(circle at 45% 40%,#f03030,#a00000 70%,rgba(160,0,0,0) 72%)}
.finance ul{position:absolute;left:158px;top:47px;list-style:none;font-size:14px;line-height:16.8px;color:var(--text-grey)}
.finance li::before{content:"•";margin-right:8px}
.finance p{position:absolute;left:158px;top:181px;width:355px;font-size:14px;line-height:17px;color:var(--text-grey)}
.goals{position:absolute;left:819px;top:163px;width:216px;height:347px;border-radius:8px;background:linear-gradient(170deg,var(--red-light),var(--red) 40%,var(--red-dark))}
.goals h3{position:absolute;left:6px;top:36px;font-weight:400;font-size:18.5px;line-height:22px;color:var(--white)}
.goals ul{list-style:none}
.goals li{position:absolute;left:12px;font-size:21.5px;line-height:23px;color:var(--white)}
.goal-tab{position:absolute;left:763px;top:278px;width:266px;height:63px}
.goal-tab span{position:absolute;left:68px;top:15px;font-size:22px;color:var(--white)}
.card{position:absolute;top:524px;width:215px;height:106px}
.card h4{width:213px;height:19px;padding-left:10px;background:linear-gradient(var(--red-light),var(--red));border-radius:3px 3px 0 0;
  font-family:"Arimo",sans-serif;font-weight:400;font-size:12.5px;line-height:19px;color:var(--white)}
.card p{position:absolute;left:5px;top:20px;width:112px;font-family:"Arimo",sans-serif;font-size:11px;line-height:13.2px;color:var(--black)}
.card-art{position:absolute;left:137px;top:24px;width:76px;height:76px;border-radius:50%}
.card-art.offers{background:radial-gradient(circle,#e02020,#a00000)}
.card-art.proposal{background:radial-gradient(circle,#fafafa 55%,#c00 60%,#800 75%,rgba(0,0,0,0) 76%)}
.card-art.browse{border-radius:30% 40% 45% 35%;background:linear-gradient(160deg,#ff3030,#b00000)}
.card-rule{position:absolute;top:515px;width:2px;height:105px;background:linear-gradient(var(--white),var(--divider) 20%,var(--divider) 80%,var(--white))}
.footer{position:absolute;left:125px;top:637px;width:925px;height:25px;background:var(--black);
  font-family:"Arimo",sans-serif;font-size:10px;line-height:25px;color:var(--white);text-align:center}
</style>
</head>
<body>
<div class="band"></div>
<div class="frame"></div>

<header class="header"></header>
<div class="logo-slot">LOGO GOES HERE</div>
<div class="search-label">SEARCH:</div>
<div class="search-field"></div>
<div class="search-go">GO</div>

<nav class="nav">
  <ul>
    <li class="current" style="left:76px">HOME</li>
    <li style="left:132px">SERVICES</li>
    <li style="left:206px">VENUES</li>
    <li style="left:268px">CLIENTS</li>
    <li style="left:332px">REGISTER</li>
    <li style="left:403px">CONTACT US</li>
  </ul>
  <div class="nav-notch" style="left:90px"></div>
</nav>

<ul class="side-menu">
  <li class="current">
    <svg width="144" height="34" viewBox="0 0 144 34"><defs><linearGradient id="tabRed" x1="0" y1="0" x2="0" y2="1"><stop offset="0" stop-color="#ff3a3a"/><stop offset="1" stop-color="#c00000"/></linearGradient></defs>
      <path d="M2 2 H128 L142 17 L128 32 H2 Z" fill="url(#tabRed)" stroke="#f3c0c0" stroke-width="2"/></svg>
    <span>OTHER MENU</span></li>
  <li><span>OTHER MENU</span></li>
  <li><span>OTHER MENU</span></li>
  <li><span>OTHER MENU</span></li>
  <li><span>OTHER MENU</span></li>
  <li><span>OTHER MENU</span></li>
</ul>
<div class="column-rule"></div>

<p class="intro"><strong>Bluegate Gatherings</strong>' professional conference team specialises in solutions. We work closely with a core group of clients to ensure desired outcomes, on time and in budget.</p>

<section class="finance">
  <h2>We offer a complete range of finance&nbsp; packages including;</h2>
  <div class="finance-art" role="img" aria-label="Red three-dimensional dollar sign illustration"></div>
  <ul>
    <li>total conference underwriting</li>
    <li>online delegate payment gateway</li>
    <li>substantially discounted rooming rates</li>
    <li>no upfront costs</li>
    <li>zero management fees</li>
    <li>free venue sourcing</li>
    <li>free delegate booking management</li>
  </ul>
  <p>Minimise your costs and free your cash flow to focus on your core business functions. We'll ensure maximum return from your conference budget.</p>
</section>

<section class="goals">
  <h3>Our goal is to make<br>sure your conference is:</h3>
  <ul>
    <li style="top:189px">Expertly Managed<br>&amp; Hassle Free</li>
    <li style="top:254px">Outcome Focussed</li>
    <li style="top:299px">Well Attended</li>
  </ul>
</section>
<div class="goal-tab">
  <svg width="266" height="63" viewBox="0 0 266 63"><defs><linearGradient id="tabDark" x1="0" y1="0" x2="0" y2="1"><stop offset="0" stop-color="#5a5a5a"/><stop offset=".5" stop-color="#3a3a3a"/><stop offset="1" stop-color="#1e1e1e"/></linearGradient></defs>
    <path d="M34 2 H258 Q264 2 264 8 V55 Q264 61 258 61 H34 L2 31.5 Z" fill="url(#tabDark)" stroke="#fff" stroke-width="3"/></svg>
  <span>Cost Effective</span>
</div>

<div class="card" style="left:283px">
  <h4>Special Offers</h4>
  <p>Not sure where to start? We have over 60 properties to choose from both domestically and international.</p>
  <div class="card-art offers" role="img" aria-label="Red starburst badge with a dollar sign"></div>
</div>
<div class="card-rule" style="left:523px"></div>
<div class="card" style="left:549px">
  <h4>Request Proposal</h4>
  <p>Not sure where to start? We have over 60 properties to choose from both domestically and international.</p>
  <div class="card-art proposal" role="img" aria-label="Red-rimmed wall clock illustration"></div>
</div>
<div class="card-rule" style="left:806px"></div>
<div class="card" style="left:822px">
  <h4>Browse Conference</h4>
  <p>Not sure where to start? We have over 60 properties to choose from both domestically and international.</p>
  <div class="card-art browse" role="img" aria-label="Glossy red map of Australia"></div>
</div>

<footer class="footer">Ph: 1300 555 012. P.O. Box 4721, Harbourview NSW 2999. Bluegate Gatherings. All Rights Reserved. 2009</footer>
</body>
</html>
```